3 out of 100 people will get deadly skin cancer - we need a great illustration that shows this!

We put together a prototype image that communicates lifetime skin cancer risk. (see attached). We are looking for illustrators who can take make a new/better/cooler graphic that communicates this idea. It could be as simple as a superior illustration of the graphic we have or illustrators can propose a completely different idea.What should the illustration communicate?U.S. adults have a lifetime risk of developing skin cancer of 1 in 5. But we don't want to show 1 in 5; we want to show that number in a larger group. For example, in the attached illustration we show 20 in 100 people get skin cancer (i.e., 100 beach towels/umbrellas and 20 of them are red). Research has shown that people are more likely to accurately understand numbers like this when you convey them for larger groups (i.e., 20 out of 100 rather than 1 out of 5). U.S. adults also have a lifetime risk of 2.3% of developing the deadliest form of skin cancer (melanoma). In other words, approximately 3 in 100 people will develop melanoma in their lifetime. Ideally, a single image will convey both lifetime skin cancer risk (20 in 100) and melanoma risk (3 in 100). We will award a top three as follows: 1st place = $300, 2nd place = $250, third place = $200. We will also buy any design beyond 3rd place that we like for $100. For example, we purchased 24 designs in our last contest on Artmarketly.This research is supported by funding from the Corvane Institute of Science.

Target Market(s)

The U.S. public; individuals at high risk of developing skin cancer

Industry/Entity Type

Medicine

Colors

Designer to choose colors to be used in the design.

Requirements
Must have
• an original illustration that conveys both lifetime risk of developing skin cancer (20 in 100) and melanoma (3 in 100).
Nice to have
• It can be beach towels and umbrellas, just like our prototype, or the designers can pitch an original idea. Imagery can be realistic or cartoonish (or something in between). It should be illustrations, though. Not edited photos. The image should be in color (no black and white illustrations).
Should not have
• Photos. Clip art. Free vector images.
• We are looking for original illustrations created by the designer.

```html
<!DOCTYPE html>
<html lang="en">
<head>
<meta charset="utf-8">
<title>Lifetime skin cancer risk — 20 in 100 seats</title>
<link rel="stylesheet" href="https://fonts.googleapis.com/css2?family=Montserrat:wght@500&display=swap">
<style>
  :root {
    --canvas: #ffffff;
    --plane-light: #eef0f6;
    --plane-mid: #d6dae3;
    --plane-edge: #bcc3cf;
    --cabin-floor: #f2f3f8;
    --cabin-line: #a9b0bb;
    --clear-body: #00a9dc;
    --clear-trim: #7fdcf7;
    --cancer-body: #a30000;
    --cancer-trim: #f25544;
    --melanoma-body: #000000;
    --melanoma-trim: #e2442f;
    --label-clear: #00a9dc;
    --label-cancer: #a30000;
    --label-melanoma: #000000;
  }
  html, body {
    margin: 0;
    padding: 0;
    width: 1200px;
    height: 1000px;
    overflow: hidden;
    background: var(--canvas);
  }
  .risk-chart {
    position: relative;
    width: 1200px;
    height: 1000px;
    font-family: "Montserrat", sans-serif;
  }
  .plane-illustration {
    position: absolute;
    left: 140px;
    top: 46px;
    width: 922px;
    height: 908px;
    border-radius: 46% 46% 30% 30% / 12% 12% 8% 8%;
    background: radial-gradient(ellipse at 50% 55%, var(--plane-mid) 0%, var(--plane-light) 45%, rgba(238,240,246,0) 72%);
  }
  .seat-map {
    position: absolute;
    left: 0;
    top: 0;
    width: 1200px;
    height: 1000px;
  }
  .cabin-floor {
    fill: var(--cabin-floor);
    stroke: var(--cabin-line);
    stroke-width: 1;
  }
  .seat-back { fill: var(--body); }
  .seat-arm, .seat-cushion { fill: var(--trim); stroke: var(--body); stroke-width: 0.6; }
  .seat-clear { --body: var(--clear-body); --trim: var(--clear-trim); }
  .seat-cancer { --body: var(--cancer-body); --trim: var(--cancer-trim); }
  .seat-melanoma { --body: var(--melanoma-body); --trim: var(--melanoma-trim); }

  .legend {
    position: absolute;
    left: 814px;
    top: 67px;
    margin: 0;
    padding: 0;
    list-style: none;
  }
  .legend-item {
    display: flex;
    align-items: center;
    height: 58px;
    margin-bottom: 22px;
  }
  .legend-icon { width: 56px; height: 58px; flex: none; }
  .legend-label {
    margin-left: 32px;
    font-size: 19px;
    font-weight: 500;
    letter-spacing: 0.2px;
  }
  .legend-label.is-clear { color: var(--label-clear); }
  .legend-label.is-cancer { color: var(--label-cancer); }
  .legend-label.is-melanoma { color: var(--label-melanoma); }
</style>
</head>
<body>
<main class="risk-chart">
  <div class="plane-illustration" role="img" aria-label="Top view of a passenger airliner with wings, engines and a boarding bridge where passengers are walking aboard"></div>

  <svg class="seat-map" viewBox="0 0 1200 1000" aria-label="Cabin of 100 seats: 17 marked skin cancer, 3 marked melanoma">
    <defs>
      <symbol id="seat" viewBox="0 0 18 20">
        <rect class="seat-back" x="1" y="0" width="16" height="17" rx="3"/>
        <rect class="seat-arm" x="0" y="2" width="2.6" height="13" rx="1.2"/>
        <rect class="seat-arm" x="15.4" y="2" width="2.6" height="13" rx="1.2"/>
        <rect class="seat-cushion" x="3" y="15" width="12" height="4.6" rx="1.2"/>
      </symbol>
    </defs>

    <rect class="cabin-floor" x="550" y="164" width="100" height="687" rx="22"/>

    <g transform="translate(0,192)"><use href="#seat" class="seat-clear" x="556" width="18" height="20"/><use href="#seat" class="seat-clear" x="576" width="18" height="20"/><use href="#seat" class="seat-clear" x="605" width="18" height="20"/><use href="#seat" class="seat-cancer" x="626" width="18" height="20"/></g>
    <g transform="translate(0,217.5)"><use href="#seat" class="seat-cancer" x="556" width="18" height="20"/><use href="#seat" class="seat-clear" x="576" width="18" height="20"/><use href="#seat" class="seat-clear" x="605" width="18" height="20"/><use href="#seat" class="seat-clear" x="626" width="18" height="20"/></g>
    <g transform="translate(0,243)"><use href="#seat" class="seat-clear" x="556" width="18" height="20"/><use href="#seat" class="seat-clear" x="576" width="18" height="20"/><use href="#seat" class="seat-clear" x="605" width="18" height="20"/><use href="#seat" class="seat-clear" x="626" width="18" height="20"/></g>
    <g transform="translate(0,268.4)"><use href="#seat" class="seat-clear" x="556" width="18" height="20"/><use href="#seat" class="seat-clear" x="576" width="18" height="20"/><use href="#seat" class="seat-cancer" x="605" width="18" height="20"/><use href="#seat" class="seat-melanoma" x="626" width="18" height="20"/></g>
    <g transform="translate(0,293.8)"><use href="#seat" class="seat-clear" x="556" width="18" height="20"/><use href="#seat" class="seat-clear" x="576" width="18" height="20"/><use href="#seat" class="seat-clear" x="605" width="18" height="20"/><use href="#seat" class="seat-clear" x="626" width="18" height="20"/></g>
    <g transform="translate(0,319.3)"><use href="#seat" class="seat-clear" x="556" width="18" height="20"/><use href="#seat" class="seat-cancer" x="576" width="18" height="20"/><use href="#seat" class="seat-clear" x="605" width="18" height="20"/><use href="#seat" class="seat-clear" x="626" width="18" height="20"/></g>
    <g transform="translate(0,344.7)"><use href="#seat" class="seat-clear" x="556" width="18" height="20"/><use href="#seat" class="seat-clear" x="576" width="18" height="20"/><use href="#seat" class="seat-clear" x="605" width="18" height="20"/><use href="#seat" class="seat-clear" x="626" width="18" height="20"/></g>
    <g transform="translate(0,370.2)"><use href="#seat" class="seat-clear" x="556" width="18" height="20"/><use href="#seat" class="seat-clear" x="576" width="18" height="20"/><use href="#seat" class="seat-clear" x="605" width="18" height="20"/><use href="#seat" class="seat-clear" x="626" width="18" height="20"/></g>
    <g transform="translate(0,395.6)"><use href="#seat" class="seat-clear" x="556" width="18" height="20"/><use href="#seat" class="seat-cancer" x="576" width="18" height="20"/><use href="#seat" class="seat-clear" x="605" width="18" height="20"/><use href="#seat" class="seat-clear" x="626" width="18" height="20"/></g>
    <g transform="translate(0,421.1)"><use href="#seat" class="seat-clear" x="556" width="18" height="20"/><use href="#seat" class="seat-clear" x="576" width="18" height="20"/><use href="#seat" class="seat-melanoma" x="605" width="18" height="20"/><use href="#seat" class="seat-clear" x="626" width="18" height="20"/></g>
    <g transform="translate(0,446.5)"><use href="#seat" class="seat-clear" x="556" width="18" height="20"/><use href="#seat" class="seat-clear" x="576" width="18" height="20"/><use href="#seat" class="seat-clear" x="605" width="18" height="20"/><use href="#seat" class="seat-clear" x="626" width="18" height="20"/></g>
    <g transform="translate(0,472)"><use href="#seat" class="seat-cancer" x="556" width="18" height="20"/><use href="#seat" class="seat-clear" x="576" width="18" height="20"/><use href="#seat" class="seat-clear" x="605" width="18" height="20"/><use href="#seat" class="seat-clear" x="626" width="18" height="20"/></g>
    <g transform="translate(0,497.4)"><use href="#seat" class="seat-cancer" x="556" width="18" height="20"/><use href="#seat" class="seat-clear" x="576" width="18" height="20"/><use href="#seat" class="seat-clear" x="605" width="18" height="20"/><use href="#seat" class="seat-clear" x="626" width="18" height="20"/></g>
    <g transform="translate(0,522.9)"><use href="#seat" class="seat-clear" x="556" width="18" height="20"/><use href="#seat" class="seat-cancer" x="576" width="18" height="20"/><use href="#seat" class="seat-cancer" x="605" width="18" height="20"/><use href="#seat" class="seat-clear" x="626" width="18" height="20"/></g>
    <g transform="translate(0,548.3)"><use href="#seat" class="seat-clear" x="556" width="18" height="20"/><use href="#seat" class="seat-clear" x="576" width="18" height="20"/><use href="#seat" class="seat-clear" x="605" width="18" height="20"/><use href="#seat" class="seat-clear" x="626" width="18" height="20"/></g>
    <g transform="translate(0,573.8)"><use href="#seat" class="seat-cancer" x="556" width="18" height="20"/><use href="#seat" class="seat-clear" x="576" width="18" height="20"/><use href="#seat" class="seat-clear" x="605" width="18" height="20"/><use href="#seat" class="seat-cancer" x="626" width="18" height="20"/></g>
    <g transform="translate(0,599.2)"><use href="#seat" class="seat-clear" x="556" width="18" height="20"/><use href="#seat" class="seat-clear" x="576" width="18" height="20"/><use href="#seat" class="seat-clear" x="605" width="18" height="20"/><use href="#seat" class="seat-clear" x="626" width="18" height="20"/></g>
    <g transform="translate(0,624.7)"><use href="#seat" class="seat-clear" x="556" width="18" height="20"/><use href="#seat" class="seat-clear" x="576" width="18" height="20"/><use href="#seat" class="seat-clear" x="605" width="18" height="20"/><use href="#seat" class="seat-cancer" x="626" width="18" height="20"/></g>
    <g transform="translate(0,650.1)"><use href="#seat" class="seat-cancer" x="556" width="18" height="20"/><use href="#seat" class="seat-clear" x="576" width="18" height="20"/><use href="#seat" class="seat-clear" x="605" width="18" height="20"/><use href="#seat" class="seat-clear" x="626" width="18" height="20"/></g>
    <g transform="translate(0,675.6)"><use href="#seat" class="seat-clear" x="556" width="18" height="20"/><use href="#seat" class="seat-clear" x="576" width="18" height="20"/><use href="#seat" class="seat-cancer" x="605" width="18" height="20"/><use href="#seat" class="seat-clear" x="626" width="18" height="20"/></g>
    <g transform="translate(0,701)"><use href="#seat" class="seat-clear" x="556" width="18" height="20"/><use href="#seat" class="seat-clear" x="576" width="18" height="20"/><use href="#seat" class="seat-clear" x="605" width="18" height="20"/><use href="#seat" class="seat-clear" x="626" width="18" height="20"/></g>
    <g transform="translate(0,726.5)"><use href="#seat" class="seat-clear" x="556" width="18" height="20"/><use href="#seat" class="seat-cancer" x="576" width="18" height="20"/><use href="#seat" class="seat-clear" x="605" width="18" height="20"/><use href="#seat" class="seat-clear" x="626" width="18" height="20"/></g>
    <g transform="translate(0,751.9)"><use href="#seat" class="seat-clear" x="556" width="18" height="20"/><use href="#seat" class="seat-clear" x="576" width="18" height="20"/><use href="#seat" class="seat-clear" x="605" width="18" height="20"/><use href="#seat" class="seat-cancer" x="626" width="18" height="20"/></g>
    <g transform="translate(0,777.4)"><use href="#seat" class="seat-cancer" x="556" width="18" height="20"/><use href="#seat" class="seat-clear" x="576" width="18" height="20"/><use href="#seat" class="seat-clear" x="605" width="18" height="20"/><use href="#seat" class="seat-clear" x="626" width="18" height="20"/></g>
    <g transform="translate(0,802.8)"><use href="#seat" class="seat-clear" x="556" width="18" height="20"/><use href="#seat" class="seat-clear" x="576" width="18" height="20"/><use href="#seat" class="seat-melanoma" x="605" width="18" height="20"/><use href="#seat" class="seat-clear" x="626" width="18" height="20"/></g>
  </svg>

  <ul class="legend">
    <li class="legend-item">
      <svg class="legend-icon" viewBox="0 0 18 20"><use href="#seat" class="seat-clear" width="18" height="20"/></svg>
      <span class="legend-label is-clear">NO SKIN CANCER</span>
    </li>
    <li class="legend-item">
      <svg class="legend-icon" viewBox="0 0 18 20"><use href="#seat" class="seat-cancer" width="18" height="20"/></svg>
      <span class="legend-label is-cancer">SKIN CANCER</span>
    </li>
    <li class="legend-item">
      <svg class="legend-icon" viewBox="0 0 18 20"><use href="#seat" class="seat-melanoma" width="18" height="20"/></svg>
      <span class="legend-label is-melanoma">MELANOMA</span>
    </li>
  </ul>
</main>
</body>
</html>
```